Altmont Self Storage Billboard

This is a 12'x24' billboard. I need this billboard to scream that it is for self storage with part of or all of the billboard having a picture of a storage unit or storage units in the background that matches my logo colors. You can use a stock image for this or I attached a picture if you would want to use that. I also need the billboard to include my logo which I have attached, the phone number of 312-647-2059, and I would like the billboard to say the following:
-Rent 100% Online at AltmontSelfStorage.com (emphasize this)
-Drive-Up & Temp-Controlled Units
-Covered & Uncovered Boat/RV Parking

I would also like there to be an arrow pointing LEFT on the bottom of the billboard that says: Willowmere Landing Apartments | 312-647-2841

```html
<!DOCTYPE html>
<html lang="en">
<head>
<meta charset="utf-8">
<title>Altmont Self Storage Billboard</title>
<link rel="stylesheet" href="https://fonts.googleapis.com/css2?family=Barlow+Condensed:wght@400;600;700&family=Lexend:wght@400&display=swap">
<style>
  :root {
    --page-bg: #eeeeee;
    --brand-blue: #0b5aa8;
    --navy: #0b1d38;
    --white: #ffffff;
    --ink: #0d1b30;
    --photo-sky: #3f78c9;
    --photo-door: #7aa7d8;
  }
  html, body {
    margin: 0;
    width: 1154px;
    height: 1200px;
    overflow: hidden;
    background: var(--page-bg);
  }
  .billboard {
    position: absolute;
    left: 27px;
    top: 326px;
    width: 1100px;
    height: 548px;
    display: block;
  }
  .brand-name { font-family: "Barlow Condensed", sans-serif; font-weight: 600; fill: var(--white); }
  .brand-phone { font-family: "Barlow Condensed", sans-serif; font-weight: 600; fill: var(--white); }
  .headline { font-family: "Barlow Condensed", sans-serif; font-weight: 700; fill: var(--white); }
  .web-lead { font-family: "Barlow Condensed", sans-serif; font-weight: 400; fill: var(--white); }
  .web-url { font-family: "Barlow Condensed", sans-serif; font-weight: 700; fill: var(--white); }
  .feature-text { font-family: "Lexend", sans-serif; font-weight: 400; fill: var(--ink); }
  .directions { font-family: "Barlow Condensed", sans-serif; font-weight: 600; fill: var(--white); }
  .directions-phone { font-weight: 700; }
</style>
</head>
<body>
<svg class="billboard" viewBox="0 0 1458 726" xmlns="http://www.w3.org/2000/svg">
  <defs>
    <linearGradient id="photoTone" x1="0" y1="0" x2="1" y2="1">
      <stop offset="0" stop-color="var(--photo-door)"/>
      <stop offset="0.55" stop-color="var(--photo-sky)"/>
      <stop offset="1" stop-color="#2d4f7e"/>
    </linearGradient>
    <linearGradient id="arrowSilver" x1="0" y1="0" x2="1" y2="0">
      <stop offset="0" stop-color="#8f9398"/>
      <stop offset="1" stop-color="#ffffff"/>
    </linearGradient>
  </defs>

  <rect class="photo-area" role="img" aria-label="Row of blue roll-up storage unit doors under a clear blue sky" x="0" y="0" width="1000" height="726" fill="url(#photoTone)"/>

  <polygon class="chevron-navy" points="620,0 1458,0 1458,726 410,726 780,175" fill="var(--navy)"/>
  <polygon class="chevron-blue" points="660,0 1458,0 1458,726 450,726 820,175" fill="var(--brand-blue)"/>
  <polygon class="chevron-white" points="690,0 720,0 870,175 520,726 490,726 840,175" fill="var(--white)"/>
  <polygon class="panel-blue" points="730,0 1458,0 1458,726 530,726 880,175" fill="var(--brand-blue)"/>

  <rect class="brand-mark" x="932" y="68" width="46" height="46" fill="var(--white)"/>
  <text class="brand-name" x="996" y="112" font-size="62">Altmont Self Storage</text>
  <text class="brand-phone" x="1190" y="170" font-size="44" text-anchor="middle">312-647-2059</text>

  <polygon class="headline-band" points="860,220 1458,220 1458,367 770,367" fill="var(--navy)"/>
  <text class="headline" x="1145" y="340" font-size="118" text-anchor="middle">Rent 100%</text>

  <polygon class="features-bg" points="740,400 1458,400 1458,615 600,615" fill="var(--white)"/>

  <path class="web-pill" d="M809,367 H1458 V435 H809 A34,34 0 0 1 809,367 Z" fill="var(--brand-blue)"/>
  <text class="web-lead" x="855" y="416" font-size="42">Online at</text>
  <g class="globe-icon" fill="none" stroke="var(--white)" stroke-width="3">
    <circle cx="1000" cy="401" r="14"/>
    <ellipse cx="1000" cy="401" rx="6" ry="14"/>
    <line x1="986" y1="401" x2="1014" y2="401"/>
    <line x1="988" y1="394" x2="1012" y2="394"/>
    <line x1="988" y1="408" x2="1012" y2="408"/>
  </g>
  <text class="web-url" x="1022" y="416" font-size="44">AltmontSelfStorage.com</text>

  <circle class="feature-icon-bg" cx="830" cy="525" r="52" fill="var(--navy)"/>
  <g class="unit-icon" fill="none" stroke="var(--white)" stroke-width="3">
    <path d="M800,555 V508 L830,490 L860,508 V555 Z"/>
    <line x1="810" y1="520" x2="850" y2="520"/>
    <rect x="812" y="526" width="16" height="22"/>
    <line x1="812" y1="537" x2="828" y2="537"/>
    <circle cx="843" cy="545" r="5"/>
    <line x1="843" y1="527" x2="843" y2="540"/>
  </g>
  <text class="feature-text" font-size="26">
    <tspan x="905" y="490">Drive-Up &amp;</tspan>
    <tspan x="905" y="522">Temperature</tspan>
    <tspan x="905" y="555">Controlled</tspan>
    <tspan x="905" y="587">Units</tspan>
  </text>

  <line class="feature-divider" x1="1101" y1="465" x2="1101" y2="590" stroke="var(--brand-blue)" stroke-width="2" stroke-dasharray="5 5"/>

  <circle class="feature-icon-bg" cx="1182" cy="525" r="52" fill="var(--navy)"/>
  <g class="vehicle-icon" fill="none" stroke="var(--white)" stroke-width="3">
    <path d="M1160,505 Q1182,494 1208,502 L1202,512 H1164 Z"/>
    <rect x="1155" y="520" width="52" height="26" rx="3"/>
    <rect x="1162" y="526" width="12" height="9"/>
    <rect x="1180" y="526" width="12" height="9"/>
    <circle cx="1166" cy="550" r="5"/>
    <circle cx="1196" cy="550" r="5"/>
  </g>
  <text class="feature-text" font-size="26">
    <tspan x="1254" y="490">Covered &amp;</tspan>
    <tspan x="1254" y="522">Uncovered</tspan>
    <tspan x="1254" y="555">Boat/RV</tspan>
    <tspan x="1254" y="587">Parking</tspan>
  </text>

  <rect class="directions-band" x="525" y="615" width="933" height="85" fill="var(--brand-blue)"/>
  <rect class="directions-rule" x="490" y="700" width="968" height="5" fill="var(--white)"/>
  <rect class="directions-base" x="478" y="705" width="980" height="21" fill="var(--navy)"/>
  <text class="directions" x="1400" y="674" font-size="44" text-anchor="end">Willowmere Landing Apartments <tspan>|</tspan> <tspan class="directions-phone">312-647-2841</tspan></text>

  <polygon class="arrow-outline" points="300,656 370,588 370,624 530,624 530,690 370,690 370,724" fill="var(--brand-blue)"/>
  <polygon class="arrow-fill" points="318,656 360,614 360,636 525,636 525,676 360,676 360,698" fill="url(#arrowSilver)"/>
</svg>
</body>
</html>
```